Rack Card for Portuguese Walking Food Tour

I would like a vertical rack card measuring 99x210mm. Here is the information I would like to include. It does not need to be in this format. We are located in Setubal, Portugal.
Please use the attached Teal Heron Logo.
Setúbal: Tradition and Today
Experience the culinary delights of Setúbal, Portugal with a walking food tour around our waterfront village. Discover the Mercado da Gaivota Branca, voted one of the world’s best markets by Metro Ledger, and indulge in local wines and dishes. Prepare for a calm stroll on flat streets. No hills to climb on this tour.
Duration: 4 hours
www.brinebasketwalks.com
+351 265 000 487

```html
<!DOCTYPE html>
<html lang="en">
<head>
<meta charset="utf-8">
<title>Walking Food Tour – Rack Card</title>
<link href="https://fonts.googleapis.com/css2?family=Alfa+Slab+One&family=Roboto+Slab:wght@300;400;700&family=Roboto+Condensed:wght@700&display=swap" rel="stylesheet">
<style>
  :root {
    --stage: #4a4a4a;
    --cream: #fdf4ea;
    --orange-top: #f26a36;
    --orange-bottom: #cd4631;
    --orange: #e9592f;
    --ghost: #d65232;
    --white: #ffffff;
    --ink: #6d6d70;
    --rule: #7a7a7d;
  }
  * { box-sizing: border-box; margin: 0; padding: 0; }
  html, body { width: 704px; height: 1200px; overflow: hidden; background: var(--stage); }
  .rack-card {
    position: absolute; left: 74px; top: 10px;
    width: 556px; height: 1180px;
    background: var(--cream);
    overflow: hidden;
  }
  .hero-band { position: absolute; left: 0; top: 0; width: 556px; height: 620px; }
  .ghost-title {
    position: absolute; left: 0; top: 0; width: 556px;
    font-family: "Alfa Slab One", serif; color: var(--ghost);
    text-align: center; line-height: 0.98; opacity: 0.75;
  }
  .ghost-title span { display: block; }
  .ghost-title .g1 { font-size: 96px; margin-top: -6px; }
  .ghost-title .g2 { font-size: 132px; }
  .ghost-title .g3 { font-size: 132px; }
  .headline {
    position: absolute; left: 0; top: 26px; width: 556px;
    font-family: "Alfa Slab One", serif; color: var(--white);
    text-align: center; text-shadow: 2px 3px 4px rgba(0,0,0,0.25);
    line-height: 1;
  }
  .headline .walking { display: block; font-size: 58px; letter-spacing: 1px; }
  .headline .food { display: block; font-size: 104px; margin-top: -2px; }
  .headline .tour { display: block; font-size: 102px; margin-top: -10px; }
  .market-photo {
    position: absolute; left: 128px; top: 281px;
    width: 320px; height: 320px; border-radius: 50%;
    border: 8px solid var(--white);
    background: radial-gradient(circle at 45% 45%, #efc3b0 0%, #e08a68 45%, #c6563c 100%);
    box-shadow: 0 14px 14px -8px rgba(0,0,0,0.25);
  }
  .highlights {
    position: absolute; left: 28px; top: 638px; width: 502px;
    list-style: none;
    font-family: "Roboto Slab", serif; font-weight: 300;
    font-size: 21px; line-height: 28px; color: var(--ink);
  }
  .highlights li { position: relative; padding-left: 29px; text-align: justify; }
  .highlights li::before { content: "•"; position: absolute; left: 0; top: 0; font-size: 16px; }
  .duration {
    position: absolute; left: 165px; top: 885px; width: 227px; height: 39px;
    background: var(--orange); color: var(--white);
    font-family: "Roboto Slab", serif; font-weight: 700; font-size: 20px;
    display: flex; align-items: center; justify-content: center;
    clip-path: polygon(0 0, 100% 0, 98% 100%, 2% 100%);
  }
  .brand {
    position: absolute; left: 0; top: 972px; width: 556px;
    display: flex; align-items: center; justify-content: center; gap: 14px;
  }
  .brand-dot { width: 40px; height: 40px; border-radius: 50%; background: var(--orange); }
  .brand-name {
    font-family: "Roboto Slab", serif; font-weight: 700; font-size: 44px;
    line-height: 1; color: var(--ink);
  }
  .phone {
    position: absolute; left: 0; top: 1066px; width: 556px;
    display: flex; align-items: center; justify-content: center; gap: 10px;
    font-family: "Roboto Condensed", sans-serif; font-weight: 700;
    font-size: 32px; color: var(--orange);
  }
  .phone svg { width: 32px; height: 32px; }
  .website {
    position: absolute; left: 48px; top: 1115px; width: 460px; height: 32px;
    border: 2px solid var(--rule);
    display: flex; align-items: center; justify-content: center;
    font-family: "Roboto Slab", serif; font-weight: 400; font-size: 16px;
    letter-spacing: 5px; color: var(--ink);
  }
  .website .domain { color: var(--orange); }
</style>
</head>
<body>
<main class="rack-card">
  <svg class="hero-band" viewBox="0 0 556 620" aria-hidden="true">
    <defs>
      <linearGradient id="bandFill" x1="0" y1="0" x2="0" y2="1">
        <stop offset="0" stop-color="var(--orange-top)"/>
        <stop offset="1" stop-color="var(--orange-bottom)"/>
      </linearGradient>
    </defs>
    <path fill="url(#bandFill)" d="M0 0 H556 V565 C480 585 420 600 340 604 L220 604 C140 600 70 585 0 560 Z"/>
  </svg>

  <div class="ghost-title" aria-hidden="true">
    <span class="g1">WALKING</span>
    <span class="g2">FOOD</span>
    <span class="g3">TOUR</span>
  </div>

  <h1 class="headline">
    <span class="walking">WALKING</span>
    <span class="food">FOOD</span>
    <span class="tour">TOUR</span>
  </h1>

  <div class="market-photo" role="img" aria-label="Photo of fresh red mullet fish piled on ice at the market"></div>

  <ul class="highlights">
    <li>Experience the culinary delights of Setúbal, Portugal with a walking food tour around our waterfront village.</li>
    <li>Discover the Mercado da Gaivota Branca, voted one of the world’s best markets by Metro Ledger, and indulge in local wines and dishes.</li>
    <li>Prepare for a calm stroll on flat streets. No hills to climb on this tour.</li>
  </ul>

  <div class="duration">Duration: 4 hours</div>

  <div class="brand">
    <span class="brand-dot" aria-hidden="true"></span>
    <span class="brand-name">Teal Heron</span>
  </div>

  <div class="phone">
    <svg viewBox="0 0 32 32" aria-hidden="true">
      <circle cx="16" cy="16" r="14.5" fill="none" stroke="var(--rule)" stroke-width="2"/>
      <path fill="var(--rule)" d="M11 9 L14 9 L15 13 L13 14.5 Q14.5 18 17.5 19 L19 17 L23 18 L23 21 Q22 23 19.5 23 Q10 21.5 9 12 Q9 9.5 11 9 Z"/>
    </svg>
    <span>+351 265 000 487</span>
  </div>

  <div class="website">WWW.<span class="domain">BRINEBASKETWALKS</span>.COM</div>
</main>
</body>
</html>
```